Business Card Design Project

I am a Chiropractor that is looking for a new business card.  Our logo was slightly changed lately, therefore need a new, more professional look.
We are a modern, non-stuffy chiropractic office.  Want a contemporary look that will let people know this is not your typical doctors office.  Our logo is red, and contains the name of our business: realign.  The u in the logo is green, stressing the most important part of our business: "u"

Target Market(s)
moderate to upper income bracket, family friendly
www.realignspine.example
Gordon Pell
Family Chiropractor
412 Birch Ave
Millbrook, TX 78690
512.555.0147 phone
512.555.0148 fax
Industry/Entity Type
Business
Requirements
Must have
- www.realignspine.example
Gordon Pell
Family Chiropractor
412 Birch Ave
Millbrook, TX 78690
512.555.0147 phone
512.555.0148 fax

```html
<!DOCTYPE html>
<html lang="en">
<head>
<meta charset="utf-8">
<title>realign business card</title>
<link href="https://fonts.googleapis.com/css2?family=Arimo:wght@400;700&display=swap" rel="stylesheet">
<style>
  :root {
    --red: #ec5b4f;
    --green: #57b150;
    --light-green: #b4d86a;
    --grey: #8a8a8a;
    --paper: #ffffff;
    --backdrop: #d9d9d6;
  }
  html, body {
    margin: 0;
    padding: 0;
    width: 1200px;
    height: 815px;
    overflow: hidden;
  }
  body {
    background: var(--backdrop);
    font-family: "Arimo", Arial, sans-serif;
    position: relative;
  }
  .card {
    position: absolute;
    top: 259px;
    width: 520px;
    height: 297px;
    background: var(--paper);
    box-shadow: 0 4px 14px rgba(0,0,0,0.18);
    overflow: hidden;
  }
  .card-back { left: 60px; display: flex; align-items: center; justify-content: center; }
  .card-front { left: 620px; }

  .wordmark {
    color: var(--red);
    font-weight: 400;
    letter-spacing: 2px;
    display: flex;
    align-items: center;
    gap: 0.3em;
  }
  .wordmark .dot {
    width: 0.45em;
    height: 0.45em;
    border-radius: 50%;
    background: var(--red);
  }
  .card-back .wordmark { font-size: 74px; }
  .card-front .wordmark { position: absolute; left: 30px; top: 26px; font-size: 28px; letter-spacing: 1px; }

  .corner-art {
    position: absolute;
    right: 0;
    top: 0;
    width: 190px;
    height: 297px;
    background: linear-gradient(160deg, var(--red) 0%, var(--light-green) 55%, var(--green) 100%);
  }

  .identity { position: absolute; left: 30px; top: 84px; }
  .name { margin: 0; color: var(--green); font-weight: 700; font-size: 27px; }
  .title { margin: 2px 0 0; color: var(--grey); font-size: 12px; }

  .contact {
    position: absolute; left: 30px; top: 158px;
    list-style: none; margin: 0; padding: 0;
    font-size: 13px; color: var(--red); line-height: 19px;
  }
  .contact li { display: flex; align-items: center; gap: 7px; }
  .contact .icon {
    width: 11px; height: 11px; background: var(--green); color: var(--paper);
    font-size: 8px; font-weight: 700; display: inline-flex; align-items: center; justify-content: center;
  }
  .address {
    position: absolute; left: 30px; top: 222px; margin: 0;
    font-style: normal; font-size: 13px; line-height: 17px; color: var(--green);
  }
</style>
</head>
<body>
  <section class="card card-back">
    <div class="wordmark"><span class="dot"></span>realign</div>
  </section>

  <section class="card card-front">
    <div class="corner-art" role="img" aria-label="Decorative corner artwork in red and green"></div>

    <div class="wordmark"><span class="dot"></span>realign</div>

    <div class="identity">
      <h1 class="name">Gordon Pell</h1>
      <p class="title">Family Chiropractor</p>
    </div>

    <ul class="contact">
      <li><span class="icon">p</span>512.555.0147</li>
      <li><span class="icon">f</span>512.555.0148</li>
      <li><span class="icon">w</span>www.realignspine.example</li>
    </ul>

    <address class="address">412 Birch Ave<br>Millbrook, TX 78690</address>
  </section>
</body>
</html>
```